Brickwell Brochure

We need a brochure on A4 to show our portfolio and invite people to take up our service offering. This brochure will be mailed to peoples home in the areas that we are targeting. We offer quick house modifications including bathroom and kitchen renovations, disability access, security, extensions and full house renovations as well as design and build services.

Target Market(s)

Home Owners, Occupational Therapists, Retirement village, Medical Centers

Industry/Entity Type

Construction and Design

Requirements
Must have
• Photos and our services listed and an invitation to use them

```html
<!DOCTYPE html>
<html lang="en">
<head>
<meta charset="utf-8">
<title>Brickwell Brochure</title>
<link rel="stylesheet" href="https://fonts.googleapis.com/css2?family=Poppins:wght@300;400;500;600;700;800&display=swap">
<style>
  :root {
    --brand-red: #c4202f;
    --brand-dark: #1c1c1e;
    --ink: #222326;
    --muted: #5a5c60;
    --paper: #ffffff;
    --stage: #e6e6e8;
  }
  * { margin: 0; padding: 0; box-sizing: border-box; }
  html, body { width: 898px; height: 1200px; overflow: hidden; background: var(--stage); }
  body { font-family: "Poppins", sans-serif; color: var(--ink); position: relative; }

  .page { position: absolute; top: 296px; width: 740px; height: 1046px; overflow: hidden; background: var(--paper);
          transform: scale(0.58); transform-origin: top left; box-shadow: 0 6px 24px rgba(0,0,0,0.25); }
  .page-front { left: 14px; }
  .page-back { left: 455px; }
  .backdrop { position: absolute; inset: 0; }

  /* front */
  .brand { position: absolute; left: 30px; top: 74px; width: 270px; text-align: center; }
  .brand-name { font-weight: 500; font-size: 46px; line-height: 1; color: var(--brand-red); }
  .brand-tag { display: flex; align-items: center; gap: 6px; margin-top: 6px; font-size: 15px; color: var(--muted); white-space: nowrap; }
  .brand-tag::before, .brand-tag::after { content: ""; flex: 1; height: 1.5px; background: var(--muted); }
  .brand-tag b { font-weight: 600; }
  .headline { position: absolute; left: 34px; top: 274px; }
  .headline-light { font-weight: 400; font-size: 36px; line-height: 45px; color: var(--ink); }
  .headline-strong { font-weight: 800; font-size: 42px; line-height: 46px; color: var(--brand-red); }
  .headline-pill { display: inline-block; margin-top: 2px; padding: 0 30px 0 18px; background: var(--brand-red); color: var(--paper);
                   font-weight: 800; font-size: 42px; line-height: 46px; border-radius: 24px; }
  .intro { position: absolute; left: 34px; top: 525px; width: 430px; font-size: 16.5px; line-height: 21px; color: var(--ink); }
  .intro strong { color: var(--brand-red); font-weight: 600; }
  .services-title { position: absolute; left: 186px; top: 658px; width: 366px; height: 42px; border-radius: 21px; background: var(--brand-dark);
                    color: var(--paper); text-align: center; font-weight: 600; font-size: 31px; line-height: 44px; }
  .services { position: absolute; left: 42px; top: 722px; display: grid; grid-template-columns: 335px 320px; row-gap: 9px; list-style: none; }
  .service { display: flex; align-items: center; gap: 14px; height: 42px; font-size: 16.5px; color: var(--ink); }
  .service-icon { width: 42px; height: 42px; flex: none; }
  .web { position: absolute; left: 0; right: 0; top: 987px; text-align: center; color: var(--paper); font-size: 17px; letter-spacing: 2px; }

  /* back */
  .why { position: absolute; left: 34px; top: 542px; }
  .why-light { font-weight: 400; font-size: 36px; line-height: 42px; color: var(--ink); }
  .why-strong { font-weight: 800; font-size: 42px; line-height: 46px; color: var(--brand-red); }
  .why-copy { position: absolute; left: 34px; top: 645px; width: 620px; font-size: 16.5px; line-height: 21px; color: var(--ink); }
  .why-copy strong { color: var(--brand-red); font-weight: 600; }
  .benefits { position: absolute; left: 34px; top: 722px; display: grid; grid-template-columns: 262px 260px; row-gap: 4px; list-style: none; }
  .benefit { display: flex; align-items: center; gap: 10px; height: 22px; font-size: 16.5px; }
  .tick { width: 18px; height: 18px; flex: none; }
  .contact-title { position: absolute; left: 0; top: 829px; width: 363px; height: 42px; padding-left: 34px; border-radius: 0 21px 21px 0;
                   background: var(--brand-red); color: var(--paper); font-weight: 700; font-size: 33px; line-height: 44px; }
  .contacts { position: absolute; left: 112px; top: 893px; display: flex; gap: 52px; font-size: 17px; }
  .contact { display: flex; align-items: center; gap: 12px; }
  .contact svg { width: 26px; height: 26px; flex: none; }
</style>
</head>
<body>

<section class="page page-front">
  <svg class="backdrop" width="740" height="1046" viewBox="0 0 740 1046">
    <defs>
      <linearGradient id="frontTop" x1="0" y1="0" x2="0" y2="1">
        <stop offset="0" stop-color="#ffffff"/><stop offset="1" stop-color="#d9d9db"/>
      </linearGradient>
      <linearGradient id="housePhoto" x1="0" y1="0" x2="0.3" y2="1">
        <stop offset="0" stop-color="#7f9bb8"/><stop offset="0.3" stop-color="#b9c2c6"/>
        <stop offset="0.6" stop-color="#9a9d9c"/><stop offset="1" stop-color="#c9c6bf"/>
      </linearGradient>
      <linearGradient id="kitchenFade" x1="0" y1="0" x2="1" y2="0">
        <stop offset="0" stop-color="#ffffff" stop-opacity="0"/><stop offset="1" stop-color="#d6d6d8"/>
      </linearGradient>
    </defs>
    <rect width="740" height="250" fill="url(#frontTop)"/>
    <path d="M0 232 C90 180 200 170 330 190 L330 280 C220 220 110 215 0 258 Z" fill="var(--paper)"/>
    <path d="M0 232 C95 176 210 166 330 186 L330 206 C210 188 100 200 0 258 Z" fill="var(--brand-red)"/>
    <rect x="430" y="470" width="310" height="200" fill="url(#kitchenFade)" role="img" aria-label="Faded photo of a bright modern kitchen"/>
    <circle cx="650" cy="160" r="362" fill="#d4d4d6" opacity="0.7"/>
    <circle cx="650" cy="168" r="340" fill="var(--brand-red)"/>
    <circle cx="650" cy="150" r="322" fill="url(#housePhoto)" role="img" aria-label="Photo of a renovated weatherboard home with an access ramp and garden path"/>
    <path d="M0 1023 C220 940 520 930 740 958 L740 1046 L0 1046 Z" fill="var(--brand-dark)"/>
    <path d="M0 1040 C220 962 520 952 740 975 L740 1046 L0 1046 Z" fill="var(--brand-red)"/>
  </svg>

  <header class="brand">
    <div class="brand-name">Brickwell</div>
    <div class="brand-tag"><span>by <b>harlow</b> builders</span></div>
  </header>

  <h1 class="headline">
    <div class="headline-light">Transforming<br>Homes Through</div>
    <div class="headline-strong">EXPERT<br>MODIFICATIONS</div>
    <div class="headline-pill">&amp; RENOVATIONS</div>
  </h1>

  <p class="intro">We deliver home modifications and renovations that enhance comfort, functionality, and style. Grow your space, modernise your layout, or refresh your home — <strong>our expert team delivers quality results from start to finish.</strong></p>

  <h2 class="services-title">OUR SERVICES</h2>

  <ul class="services">
    <li class="service"><svg class="service-icon" viewBox="0 0 50 50"><circle cx="25" cy="25" r="22" fill="none" stroke="var(--brand-red)" stroke-width="2"/><path d="M15 26 L25 17 L35 26 M18 24 V34 H32 V24" fill="none" stroke="var(--brand-red)" stroke-width="2"/></svg>Quick House Modifications</li>
    <li class="service"><svg class="service-icon" viewBox="0 0 50 50"><circle cx="25" cy="25" r="22" fill="none" stroke="var(--brand-red)" stroke-width="2"/><rect x="15" y="20" width="20" height="14" fill="none" stroke="var(--brand-red)" stroke-width="2"/><path d="M19 20 V15 H31 V20" fill="none" stroke="var(--brand-red)" stroke-width="2"/></svg>Bathroom Renovations</li>
    <li class="service"><svg class="service-icon" viewBox="0 0 50 50"><circle cx="25" cy="25" r="22" fill="none" stroke="var(--brand-red)" stroke-width="2"/><rect x="14" y="22" width="22" height="12" fill="none" stroke="var(--brand-red)" stroke-width="2"/><path d="M14 27 H36 M20 18 V22 M30 18 V22" fill="none" stroke="var(--brand-red)" stroke-width="2"/></svg>Kitchen Renovations</li>
    <li class="service"><svg class="service-icon" viewBox="0 0 50 50"><circle cx="25" cy="25" r="22" fill="none" stroke="var(--brand-red)" stroke-width="2"/><circle cx="25" cy="22" r="6" fill="none" stroke="var(--brand-red)" stroke-width="2"/><path d="M14 32 C20 36 26 36 36 30" fill="none" stroke="var(--brand-red)" stroke-width="2"/></svg>Disability Access</li>
    <li class="service"><svg class="service-icon" viewBox="0 0 50 50"><circle cx="25" cy="25" r="22" fill="none" stroke="var(--brand-red)" stroke-width="2"/><path d="M25 13 L35 17 V25 C35 31 30 35 25 37 C20 35 15 31 15 25 V17 Z" fill="none" stroke="var(--brand-red)" stroke-width="2"/><rect x="21" y="23" width="8" height="7" fill="var(--brand-red)"/></svg>Security</li>
    <li class="service"><svg class="service-icon" viewBox="0 0 50 50"><circle cx="25" cy="25" r="22" fill="none" stroke="var(--brand-red)" stroke-width="2"/><path d="M14 25 L24 16 L34 25 M17 23 V34 H31 V23" fill="none" stroke="var(--brand-red)" stroke-width="2"/><path d="M34 30 H38 M36 28 V32" stroke="var(--brand-red)" stroke-width="2"/></svg>Extensions</li>
    <li class="service"><svg class="service-icon" viewBox="0 0 50 50"><circle cx="25" cy="25" r="22" fill="none" stroke="var(--brand-red)" stroke-width="2"/><path d="M14 25 L25 15 L36 25 M17 23 V35 H33 V23" fill="none" stroke="var(--brand-red)" stroke-width="2"/><circle cx="25" cy="28" r="4" fill="none" stroke="var(--brand-red)" stroke-width="2"/></svg>Full House Renovations</li>
    <li class="service"><svg class="service-icon" viewBox="0 0 50 50"><circle cx="25" cy="25" r="22" fill="none" stroke="var(--brand-red)" stroke-width="2"/><path d="M14 25 L25 15 L36 25 M17 23 V35 H33 V23" fill="none" stroke="var(--brand-red)" stroke-width="2"/><path d="M21 33 L29 25" stroke="var(--brand-red)" stroke-width="2"/></svg>Design &amp; Build Services</li>
  </ul>

  <footer class="web">www.brickwell.com.au</footer>
</section>

<section class="page page-back">
  <svg class="backdrop" width="740" height="1046" viewBox="0 0 740 1046">
    <defs>
      <linearGradient id="bathPhoto" x1="0" y1="0" x2="0.4" y2="1">
        <stop offset="0" stop-color="#f2f2f0"/><stop offset="0.5" stop-color="#dcdad6"/>
        <stop offset="0.75" stop-color="#c99a5c"/><stop offset="1" stop-color="#a8a5a2"/>
      </linearGradient>
      <linearGradient id="diningPhoto" x1="0" y1="0" x2="0" y2="1">
        <stop offset="0" stop-color="#f4f4f4"/><stop offset="0.45" stop-color="#4a6a6c"/>
        <stop offset="0.65" stop-color="#c0803e"/><stop offset="1" stop-color="#7a5836"/>
      </linearGradient>
      <linearGradient id="sinkPhoto" x1="0" y1="0" x2="0" y2="1">
        <stop offset="0" stop-color="#8d9290"/><stop offset="0.5" stop-color="#d9dbdc"/><stop offset="1" stop-color="#e8e8e8"/>
      </linearGradient>
      <linearGradient id="vanityFade" x1="0" y1="0" x2="1" y2="0">
        <stop offset="0" stop-color="#ffffff" stop-opacity="0"/><stop offset="1" stop-color="#dcdcde"/>
      </linearGradient>
    </defs>
    <path d="M0 0 H740 V400 C500 380 240 360 0 470 Z" fill="url(#bathPhoto)" role="img" aria-label="Photo of a renovated bathroom with twin basins and timber vanity"/>
    <path d="M0 440 C130 390 260 370 400 372 L400 410 C260 410 120 450 0 565 Z" fill="var(--brand-dark)"/>
    <path d="M430 0 H740 V70 C640 40 540 30 430 60 Z" fill="var(--brand-dark)"/>
    <rect x="420" y="690" width="320" height="130" fill="url(#vanityFade)" role="img" aria-label="Faded photo of a bathroom shelf with toiletries"/>
    <circle cx="690" cy="250" r="282" fill="#d4d4d6"/>
    <circle cx="680" cy="250" r="266" fill="var(--brand-red)"/>
    <circle cx="690" cy="250" r="244" fill="url(#diningPhoto)" role="img" aria-label="Photo of an open kitchen with a timber dining table and wire chairs"/>
    <circle cx="259" cy="393" r="145" fill="var(--brand-red)"/>
    <circle cx="259" cy="393" r="131" fill="var(--paper)"/>
    <circle cx="259" cy="393" r="122" fill="url(#sinkPhoto)" role="img" aria-label="Photo of a black kitchen sink with a matte black tap by a window"/>
    <path d="M0 1023 C220 940 520 930 740 958 L740 1046 L0 1046 Z" fill="var(--brand-dark)"/>
    <path d="M0 1040 C220 962 520 952 740 975 L740 1046 L0 1046 Z" fill="var(--brand-red)"/>
  </svg>

  <h2 class="why">
    <div class="why-light">Why</div>
    <div class="why-strong">CHOOSE US?</div>
  </h2>

  <p class="why-copy">With over <strong>10 years</strong> of experience across the <strong>Mornington Peninsula</strong> and <strong>Melbourne,</strong> we deliver high-quality results backed by proven expertise and a commitment to excellence.</p>

  <ul class="benefits">
    <li class="benefit"><svg class="tick" viewBox="0 0 18 18"><rect x="1" y="3" width="14" height="14" fill="none" stroke="var(--ink)" stroke-width="1.6"/><path d="M4 9 L8 13 L17 2" fill="none" stroke="var(--ink)" stroke-width="2"/></svg>Full Service</li>
    <li class="benefit"><svg class="tick" viewBox="0 0 18 18"><rect x="1" y="3" width="14" height="14" fill="none" stroke="var(--ink)" stroke-width="1.6"/><path d="M4 9 L8 13 L17 2" fill="none" stroke="var(--ink)" stroke-width="2"/></svg>Clear Communication</li>
    <li class="benefit"><svg class="tick" viewBox="0 0 18 18"><rect x="1" y="3" width="14" height="14" fill="none" stroke="var(--ink)" stroke-width="1.6"/><path d="M4 9 L8 13 L17 2" fill="none" stroke="var(--ink)" stroke-width="2"/></svg>Fixed Pricing</li>
    <li class="benefit"><svg class="tick" viewBox="0 0 18 18"><rect x="1" y="3" width="14" height="14" fill="none" stroke="var(--ink)" stroke-width="1.6"/><path d="M4 9 L8 13 L17 2" fill="none" stroke="var(--ink)" stroke-width="2"/></svg>Quality Trades</li>
    <li class="benefit"><svg class="tick" viewBox="0 0 18 18"><rect x="1" y="3" width="14" height="14" fill="none" stroke="var(--ink)" stroke-width="1.6"/><path d="M4 9 L8 13 L17 2" fill="none" stroke="var(--ink)" stroke-width="2"/></svg>Detailed Work Scope</li>
    <li class="benefit"><svg class="tick" viewBox="0 0 18 18"><rect x="1" y="3" width="14" height="14" fill="none" stroke="var(--ink)" stroke-width="1.6"/><path d="M4 9 L8 13 L17 2" fill="none" stroke="var(--ink)" stroke-width="2"/></svg>Track Record</li>
  </ul>

  <h2 class="contact-title">CONTACT INFO:</h2>

  <div class="contacts">
    <div class="contact"><svg viewBox="0 0 26 26"><path d="M6 3 L10 3 L12 9 L9 11 C10 14 12 16 15 17 L17 14 L23 16 L23 20 C23 22 21 23 19 23 C10 22 4 16 3 7 C3 5 4 3 6 3 Z" fill="var(--brand-red)"/><path d="M16 4 C19 5 21 7 22 10 M16 8 C17 8.5 18 9.5 18.5 11" fill="none" stroke="var(--brand-red)" stroke-width="1.6"/></svg>(03) 5550-1842</div>
    <div class="contact"><svg viewBox="0 0 26 26"><rect x="2" y="6" width="22" height="15" fill="none" stroke="var(--brand-red)" stroke-width="2"/><path d="M2 6 L13 15 L24 6 M2 21 L10 13 M24 21 L16 13" fill="none" stroke="var(--brand-red)" stroke-width="2"/></svg>info@brickwell.com.au</div>
  </div>

  <footer class="web">www.brickwell.com.au</footer>
</section>

</body>
</html>
```